Shine Bay Auto Care Business Card

2 side business card design for an auto detailing business

Target Market(s)

Auto detailing

Contact Information for Business Card

Things included

The business name “Shine Bay Auto Care”
Marc Tessier
(403)261-9047
Kestrel Falls, Sk

Services offered - complete interior& exterior detail
- paint correction & protection
- ceramic coating
- trim restore
- auto carpet & seat cleaning

Requirements
Must have
• Colours that are in my logo

Services offered

My name Marc Tessier
403-261-9047
Kestrel Falls, Sk

Not too sure in what order for these ?
Website. Shinebayautocare.com
Instagram Shinebayautocare
Email. Shinebayautoac@mailbox-example.com

```html
<!DOCTYPE html>
<html lang="en">
<head>
<meta charset="utf-8">
<title>Shine Bay Auto Care – Business Card</title>
<link rel="stylesheet" href="https://fonts.googleapis.com/css2?family=Montserrat:wght@600;700&family=Poppins:wght@300;400&display=swap">
<style>
  :root {
    --stage: #2b2b2d;
    --card: #161617;
    --card-edge: #1f1f21;
    --red: #a61e22;
    --red-soft: #8e1a1d;
    --white: #f4f4f4;
    --rule: #8a8a8a;
  }
  * { box-sizing: border-box; margin: 0; padding: 0; }
  html, body {
    width: 1200px; height: 900px; overflow: hidden;
    background: var(--stage);
  }
  .stage {
    width: 1200px; height: 900px;
    display: flex; flex-direction: column; align-items: center; justify-content: center;
    gap: 40px;
  }
  .card {
    position: relative; width: 700px; height: 400px; overflow: hidden;
    background: radial-gradient(ellipse at 40% 35%, var(--card-edge) 0%, var(--card) 70%);
    box-shadow: 0 10px 30px rgba(0,0,0,.55);
    color: var(--white);
  }

  /* Front */
  .brand {
    position: absolute; left: 50px; top: 150px; width: 260px;
    display: flex; align-items: center; gap: 16px;
  }
  .brand-dot {
    flex: none; width: 58px; height: 58px; border-radius: 50%;
    border: 7px solid var(--red);
  }
  .brand-name {
    font-family: "Montserrat", sans-serif; font-weight: 700;
    font-size: 26px; line-height: 1.1; text-transform: uppercase;
    color: var(--white); letter-spacing: .5px;
  }
  .divider {
    position: absolute; left: 335px; top: 90px; width: 1px; height: 220px;
    background: var(--rule);
  }
  .contact { position: absolute; left: 362px; top: 110px; width: 320px; }
  .person {
    font-family: "Montserrat", sans-serif; font-weight: 600;
    font-size: 24px; letter-spacing: 1px; text-transform: uppercase;
  }
  .person-bar { width: 26px; height: 3px; background: var(--red); margin: 8px 0 14px; }
  .contact-list { list-style: none; }
  .contact-item {
    display: flex; align-items: center; gap: 10px; margin-bottom: 9px;
    font-family: "Poppins", sans-serif; font-weight: 300; font-size: 13px;
    white-space: nowrap;
  }
  .contact-icon { flex: none; width: 20px; height: 20px; }

  /* Back */
  .back-ring {
    position: absolute; left: -150px; top: -20px; width: 440px; height: 440px;
    border-radius: 50%; border: 34px solid var(--red);
  }
  .back-name {
    position: absolute; left: 40px; top: 182px; width: 210px;
    font-family: "Montserrat", sans-serif; font-weight: 700;
    font-size: 20px; line-height: 1.15; text-transform: uppercase; color: var(--white);
  }
  .services { position: absolute; left: 310px; top: 62px; list-style: none; }
  .service {
    display: flex; align-items: center; gap: 16px; margin-bottom: 16px;
    font-family: "Montserrat", sans-serif; font-weight: 700; font-size: 14px;
    text-transform: uppercase; letter-spacing: .5px; white-space: nowrap;
  }
  .service-badge {
    flex: none; width: 58px; height: 58px; border-radius: 50%;
    border: 3px solid var(--red);
    background: radial-gradient(circle, var(--red-soft) 0 45%, transparent 46%);
  }
</style>
</head>
<body>
<main class="stage">
  <section class="card card-front" aria-label="Card front">
    <div class="brand">
      <span class="brand-dot"></span>
      <span class="brand-name">Shine Bay Auto Care</span>
    </div>
    <div class="divider"></div>
    <div class="contact">
      <h1 class="person">Marc Tessier</h1>
      <div class="person-bar"></div>
      <ul class="contact-list">
        <li class="contact-item">
          <svg class="contact-icon" viewBox="0 0 20 20"><circle cx="10" cy="10" r="9" fill="none" stroke="#a61e22" stroke-width="1.5"/><path d="M7 5.5c-1 1-1 3 1 5.5s4 3.5 5.5 2.5l-1.3-1.8-1.4.7c-.8-.4-2-1.8-2.2-2.6l.8-1.3z" fill="#a61e22"/></svg>
          403-261-9047
        </li>
        <li class="contact-item">
          <svg class="contact-icon" viewBox="0 0 20 20"><circle cx="10" cy="10" r="9" fill="none" stroke="#a61e22" stroke-width="1.5"/><rect x="5.5" y="6.5" width="9" height="7" fill="none" stroke="#a61e22" stroke-width="1.3"/><path d="M5.5 6.5l4.5 4 4.5-4" fill="none" stroke="#a61e22" stroke-width="1.3"/></svg>
          Shinebayautocare@mailbox-example.com
        </li>
        <li class="contact-item">
          <svg class="contact-icon" viewBox="0 0 20 20"><circle cx="10" cy="10" r="9" fill="none" stroke="#a61e22" stroke-width="1.5"/><circle cx="10" cy="10" r="5" fill="none" stroke="#a61e22" stroke-width="1.2"/><path d="M5 10h10M10 5c-2 3-2 7 0 10M10 5c2 3 2 7 0 10" fill="none" stroke="#a61e22" stroke-width="1"/></svg>
          Shinebayautocare.com
        </li>
        <li class="contact-item">
          <svg class="contact-icon" viewBox="0 0 20 20"><circle cx="10" cy="10" r="9" fill="none" stroke="#a61e22" stroke-width="1.5"/><circle cx="10" cy="10" r="4" fill="none" stroke="#a61e22" stroke-width="1.3"/></svg>
          Shinebayautocare
        </li>
        <li class="contact-item">
          <svg class="contact-icon" viewBox="0 0 20 20"><circle cx="10" cy="10" r="9" fill="none" stroke="#a61e22" stroke-width="1.5"/><path d="M10 15s-4-4-4-6.5a4 4 0 0 1 8 0C14 11 10 15 10 15z" fill="#a61e22"/><circle cx="10" cy="8.5" r="1.4" fill="#161617"/></svg>
          Kestrel Falls, Sk
        </li>
      </ul>
    </div>
  </section>

  <section class="card card-back" aria-label="Card back">
    <div class="back-ring"></div>
    <div class="back-name">Shine Bay Auto Care</div>
    <ul class="services">
      <li class="service"><span class="service-badge" role="img" aria-label="Icon of a car being polished"></span>Paint Correction &amp; Protection</li>
      <li class="service"><span class="service-badge" role="img" aria-label="Icon of a car being coated"></span>Ceramic Coating</li>
      <li class="service"><span class="service-badge" role="img" aria-label="Icon of a hand restoring trim"></span>Trim Restore</li>
      <li class="service"><span class="service-badge" role="img" aria-label="Icon of a car seat being cleaned"></span>Auto Carpet &amp; Seat Cleaning</li>
    </ul>
  </section>
</main>
</body>
</html>
```